Your complete Gardening and lawn maintenance, Horticultural care. (to be on card)
We are looking at using a logo of a tree, with a recycling emblem circling the tree. The colors of choice, are burnt oranges and olive greens. Presented; simple to the eye, yet catchy to the clients in a eco-friendly way. We have uploaded a design for you to look at just to give a rough idea, you can use that or create your own ideas or play around with a mixture.

Target Market(s)

Home owners, businesses, real estates.

Industry/Entity Type

Recycling

Contact Information for Business Card

Name: Derek Ostrowe
Phone: 0421583906
Email: bramblewoodyards@mailnest.net

Logo Text

Bramble-Wood Yards

Logo styles of interest
Emblem Logo
Pictorial/Combination Logo
Abstract Logo
Requirements
Must have
• Business name: Bramble-Wood Yards
and slogan : Your complete Gardening and lawn maintenance, Horticultural care

```html
<!DOCTYPE html>
<html lang="en">
<head>
<meta charset="utf-8">
<title>Bramble-Wood Yards – Business Cards</title>
<link rel="stylesheet" href="https://fonts.googleapis.com/css2?family=Arimo:wght@500;600&family=Outfit:wght@300;400&display=swap">
<style>
  :root {
    --backdrop: #e6e7e9;
    --orange-light: #ec5f2a;
    --orange-deep: #b8482a;
    --olive-light: #b4bd35;
    --olive-deep: #646829;
    --mark-olive: #a9bd3a;
    --ink-white: #ffffff;
  }
  html, body {
    margin: 0;
    padding: 0;
    width: 1200px;
    height: 1000px;
    overflow: hidden;
    background: var(--backdrop);
  }
  .stage { position: relative; width: 1200px; height: 1000px; }
  .card {
    position: absolute;
    display: block;
    box-shadow: 4px 5px 6px rgba(0,0,0,0.35);
  }
  .card--portrait { left: 54px; top: 173px; width: 377px; height: 654px; }
  .card--landscape { left: 492px; top: 450px; width: 654px; height: 377px; }
  .brand-name { font-family: "Arimo", Arial, sans-serif; font-weight: 600; font-size: 30px; fill: var(--ink-white); }
  .slogan { font-family: "Arimo", Arial, sans-serif; font-weight: 600; font-size: 16.5px; fill: var(--ink-white); }
  .rule { stroke: var(--ink-white); stroke-width: 2; }
  .person { font-family: "Outfit", sans-serif; font-weight: 400; font-size: 26px; fill: var(--ink-white); }
  .contact { font-family: "Outfit", sans-serif; font-weight: 300; font-size: 17px; fill: var(--ink-white); }
  .mark-dot { fill: var(--mark-olive); }
</style>
</head>
<body>
<main class="stage">
  <svg class="card card--portrait" viewBox="0 0 377 654" xmlns="http://www.w3.org/2000/svg">
    <defs>
      <linearGradient id="portraitOrange" x1="0" y1="0" x2="0" y2="1">
        <stop offset="0" stop-color="var(--orange-light)"/>
        <stop offset="0.7" stop-color="var(--orange-deep)"/>
      </linearGradient>
      <linearGradient id="portraitOlive" x1="1" y1="0" x2="0" y2="1">
        <stop offset="0" stop-color="var(--olive-light)"/>
        <stop offset="1" stop-color="var(--olive-deep)"/>
      </linearGradient>
    </defs>
    <rect class="card-base" width="377" height="654" fill="url(#portraitOrange)"/>
    <path class="card-wave" d="M0,197 C90,250 140,380 200,410 C260,440 330,450 377,455 L377,654 L0,654 Z" fill="url(#portraitOlive)"/>
    <circle class="mark-dot" cx="189" cy="237" r="62"/>
    <text class="brand-name" x="188.5" y="345" text-anchor="middle">Bramble-Wood Yards</text>
    <line class="rule" x1="42" y1="356" x2="333" y2="356"/>
    <text class="slogan" x="186" y="379" text-anchor="middle">Your complete Gardening and</text>
    <text class="slogan" x="186" y="400" text-anchor="middle">lawn maintenance, Horticultural care</text>
    <text class="person" x="43" y="545">Derek Ostrowe</text>
    <text class="contact" x="43" y="579">P: 0421583906</text>
    <text class="contact" x="43" y="613">E: bramblewoodyards@mailnest.net</text>
  </svg>

  <svg class="card card--landscape" viewBox="0 0 654 377" xmlns="http://www.w3.org/2000/svg">
    <defs>
      <linearGradient id="landscapeOrange" x1="0" y1="0" x2="0" y2="1">
        <stop offset="0" stop-color="var(--orange-light)"/>
        <stop offset="0.75" stop-color="var(--orange-deep)"/>
      </linearGradient>
      <linearGradient id="landscapeOlive" x1="0" y1="0" x2="0.3" y2="1">
        <stop offset="0" stop-color="var(--olive-light)"/>
        <stop offset="1" stop-color="var(--olive-deep)"/>
      </linearGradient>
    </defs>
    <rect class="card-base" width="654" height="377" fill="url(#landscapeOrange)"/>
    <path class="card-wave" d="M0,262 C150,250 300,235 420,200 C520,170 600,140 654,115 L654,377 L0,377 Z" fill="url(#landscapeOlive)"/>
    <circle class="mark-dot" cx="153" cy="127" r="62"/>
    <text class="brand-name" x="410" y="112" text-anchor="middle">Bramble-Wood Yards</text>
    <line class="rule" x1="265" y1="123" x2="555" y2="123"/>
    <text class="slogan" x="410" y="146" text-anchor="middle">Your complete Gardening and</text>
    <text class="slogan" x="410" y="167" text-anchor="middle">lawn maintenance, Horticultural care</text>
    <text class="person" x="620" y="268" text-anchor="end">Derek Ostrowe</text>
    <text class="contact" x="620" y="302" text-anchor="end">P: 0421583906</text>
    <text class="contact" x="620" y="336" text-anchor="end">E: bramblewoodyards@mailnest.net</text>
  </svg>
</main>
</body>
</html>
```